BrightCareWorks.com, a web based eHealth startup, needs a URL landing page.

We will be building a portfolio of mocked up website screen shots of our products that we will use to engage prospective customers. We would like to start with the company's URL landing page in order to quickly capture a client's interest and identify a graphic artist that we think has the understanding of the feel/UI we are looking for and the talent to meet our expectations. The two solutions we would like to showcase are "BrightCareDialogue" (BCD) and "BrightCareCircle" (BCC).

BCD is a product for improving hospital inpatient communication using tablets and smart phones. Key descriptors for this solution would be, "Improve communication between the patient, the health care team, and the family care team", "Improve communication between Health Team members", and "Monitor for success and improvement opportunities of administrative goals using direct patient feedback."

BCC is a product for improving patient communication after discharge using tablets, smart phones, and computers. Key descriptors for this solution would be, "Transition support to the Family Care Team", "Stay connected after discharge by creating a CareCircle of support", and "Monitor progress, provide encouragement, and coordinate support of loved ones"

The goal of the site will be to give potential customers the impression/feeling of great communication, happiness, and health to patients and staff in the hospital and patients, family, and health care providers outside of the hospital. We are hoping to build a relationship with a talented graphic artist as we continue to grow.
Updates

                                        Hello all, I'm trying to upload a logo file to the project brief, but I'm having a little trouble. I have contacted customer service to request a little help. I will also try and find some examples of pages that may have the look I was thinking of. I didn't try to find anything at the start of the project because I was interested to see if there was a design that I may not have thought of. I can certainly try to find some examples though. As for the logo, I tried to put something together on Photoshop, though I also did one on PowerPoint. All I did for now was use BrightCareWroks where the My was in freestyle script, Health was in Adobe Caslon, the e at the end of Health was in freestyle script again, and the Solutions was in Adobe Caslon again. I also made the freestyle script a bright blue and the Adobe Caslon black in color. This was just what I tried first. Underneath the script I had three circles overlapping so that the point at which they all intersected was in the shape of a shield. This symbol stood for "patient centered care". I guess I'll be posting a project for a logo design soon as well to help refine this. This is my first time using a design site like this so I apologize if there is information needed that I have not provided in a easy to use format. I will certainly extend the deadline if more time is needed.  Thank you and please feel free to send any messages or comments. Thanks again.  

Industry/Entity Type

Building

Requirements
Must have
• A banner with scrolling pictures depicting scenes of patients of all ages happily interacting with hospital health team members, people (patients and nurses/doctors) using tablets, smart phones, and computers in the in the hospital, and patients (elderly and 10-15 years old) using happily using a tablet, smart phone, and/or computer.
• Clean, clutter free look.
• Buttons for [Home], [Solutions], [Platform Model], and [Contact Us].

```html
<!DOCTYPE html>
<html lang="en">
<head>
<meta charset="utf-8">
<title>BrightCareWorks</title>
<link href="https://fonts.googleapis.com/css2?family=Oswald:wght@300;400;600&display=swap" rel="stylesheet">
<style>
:root{
  --brand:#11a3cc;
  --brand-dark:#0a7fa3;
  --banner-top:#19a9d2;
  --banner-bottom:#93dbf0;
  --footer:#b9e4f2;
  --field:#a6dbec;
  --text:#555b60;
  --white:#ffffff;
}
*{margin:0;padding:0;box-sizing:border-box}
html,body{width:784px;height:1200px;overflow:hidden;background:var(--white)}
body{position:relative;font-family:Arial,Helvetica,sans-serif;color:var(--text)}
.abs{position:absolute}
.display{font-family:'Oswald',sans-serif}

.topbar{left:0;top:0;width:784px;height:70px;background:linear-gradient(#fff,#eef4f7)}
.brand{left:22px;top:10px;display:flex;align-items:center;gap:6px}
.brand-dot{width:50px;height:50px;border-radius:50%;background:var(--brand)}
.brand-name{font-family:'Oswald',sans-serif;font-weight:400;font-size:15px;color:var(--brand)}
.nav{left:117px;top:22px;height:48px;display:flex}
.nav a{font-family:'Oswald',sans-serif;font-weight:300;font-size:20px;color:var(--brand);text-decoration:none;padding:9px 17px 0;height:48px}
.nav a.active{background:var(--brand);color:var(--white);border-radius:4px 4px 0 0;padding:9px 20px 0}

.banner{left:0;top:70px;width:784px;height:376px;background:linear-gradient(var(--banner-top),var(--banner-bottom))}
.banner-photo{left:0;top:55px;width:414px;height:321px;background:linear-gradient(135deg,#e9d3c4,#c9a9a0 55%,#3c4a66);border-radius:180px 140px 0 0}
.banner-title{left:366px;top:172px;font-family:'Oswald',sans-serif;font-weight:600;font-size:40px;color:var(--white);letter-spacing:-0.5px}
.banner-text{left:367px;top:228px;width:350px;font-family:'Oswald',sans-serif;font-weight:300;font-size:27px;line-height:29px;color:var(--white)}
.dots{left:681px;top:415px;display:flex;gap:13px}
.dots span{width:18px;height:18px;border-radius:50%;background:var(--brand)}
.dots span.on{background:var(--white)}
.banner-shade{left:0;top:446px;width:784px;height:26px;background:linear-gradient(#eaf3f6,#fff)}

.devices{left:44px;top:524px;width:258px;height:188px;background:linear-gradient(135deg,#2b2f33,#5a6066);border-radius:10px}
.product{left:406px;width:372px}
.product h2{font-family:'Oswald',sans-serif;font-weight:300;font-size:26px;color:var(--brand);line-height:1}
.product h2 b{font-weight:600}
.product p{margin-top:8px;font-size:10.5px;line-height:13.5px}

.about{left:45px;top:780px;width:712px}
.about h1{font-family:'Oswald',sans-serif;font-weight:300;font-size:40px;color:var(--brand);line-height:1}
.about p{margin-top:12px;font-size:10.5px;line-height:13.5px}
.btn{display:inline-block;background:var(--brand);color:var(--white);font-family:'Oswald',sans-serif;font-weight:600;border-radius:5px;text-align:center}
.more{left:45px;top:901px;width:61px;height:27px;font-size:14px;line-height:27px}

.footer{left:0;top:996px;width:784px;height:204px;background:var(--footer)}
.foot-h{font-family:'Oswald',sans-serif;font-weight:600;font-size:15px;color:var(--brand-dark)}
.foot-links{left:26px;top:1053px;font-size:10px;line-height:11.6px;color:var(--brand-dark)}
.field{left:246px;width:208px;border:1px solid #8ecde2;border-radius:4px;background:var(--field);font-size:10px;font-weight:bold;color:var(--brand-dark);padding:6px 10px}
.submit{left:243px;top:1164px;width:62px;height:20px;font-family:Arial,sans-serif;font-size:10px;font-weight:bold;line-height:20px;border-radius:6px}
.contact{left:563px;top:1050px;font-size:10px;line-height:11.6px;color:var(--brand-dark)}
.social{left:561px;top:1122px;display:flex;gap:5px}
.social span{width:25px;height:25px;border-radius:3px;background:#5e8fa3}
</style>
</head>
<body>
<header>
  <div class="abs topbar"></div>
  <div class="abs brand"><span class="brand-dot"></span></div>
  <nav class="abs nav">
    <a class="active" href="#">HOME</a><a href="#">ABOUT US</a><a href="#">SOLUTIONS</a><a href="#">PLATFORM MODEL</a><a href="#">CONTACT US</a>
  </nav>
</header>

<section>
  <div class="abs banner"></div>
  <div class="abs banner-photo" role="img" aria-label="Smiling elderly patient with a nurse leaning beside her"></div>
  <h1 class="abs banner-title">Stay Connected</h1>
  <p class="abs banner-text">Stay connected after discharge by creating a CareCircle of support.</p>
  <div class="abs dots"><span></span><span></span><span class="on"></span></div>
  <div class="abs banner-shade"></div>
</section>

<section>
  <div class="abs devices" role="img" aria-label="Tablet and smartphone showing the BrightCareDialogue and BrightCareCircle apps"></div>
  <div class="abs product" style="top:516px">
    <h2><b>BCD</b> ‘BrightCareDialogue’</h2>
    <p>BCD offers Improve communication between the patient, the health care team, and the family care team", "Improve communication between Health Team members", and "Monitor for success and improvement opportunities of administrative goals using direct patient feedback.</p>
  </div>
  <div class="abs product" style="top:628px">
    <h2><b>BCC</b> ‘BrightCareCircle’</h2>
    <p>Transition support to the Family Care Team", "Stay connected after discharge by creating a CareCircle of support", and "Monitor progress, provide encouragement, and coordinate support of loved ones</p>
  </div>
</section>

<section class="abs about">
  <h1>ABOUT US</h1>
  <p>Lorem ipsum dolor sit amet, consectetur adipisicing elit, sed do eiusmod tempor incididunt ut labore et dolore magna aliqua. Ut enim ad minim veniam, quis nostrud exercitation ullamco laboris nisi ut aliquip ex ea commodo consequat. Lorem ipsum dolor sit amet, consectetur adipisicing elit, sed do eiusmod tempor incididunt ut labore et dolore magna aliqua. Ut enim ad minim veniam, quis nostrud exercitation ullamco laboris nisi ut aliquip ex ea commodo consequat.</p>
</section>
<a class="abs btn more" href="#">more</a>

<footer>
  <div class="abs footer"></div>
  <h3 class="abs foot-h" style="left:24px;top:1026px">NAVIGATION</h3>
  <div class="abs foot-links">HOME<br>ABOUT US<br>SOLUTIONS<br>PLATFORM MODEL<br>CONTACT US</div>

  <h3 class="abs foot-h" style="left:247px;top:1026px">EMAIL US</h3>
  <div class="abs field" style="top:1050px;height:23px">email</div>
  <div class="abs field" style="top:1077px;height:22px">subject</div>
  <div class="abs field" style="top:1103px;height:55px">content</div>
  <a class="abs btn submit" href="#">submit</a>

  <h3 class="abs foot-h" style="left:559px;top:1026px">CONTACT US</h3>
  <div class="abs contact">12 Marlow Park Road, Fenbridge,<br>FB2 4KT, UK<br>Tel: +44 20 5550 1180<br>Fax: +44 20 5550 1181<br>Mail: info@BrightCareWorks.com</div>
  <div class="abs social"><span></span><span></span><span></span><span></span><span></span></div>
</footer>
</body>
</html>
```